Veltorquin.io - Please redesign to make it look better from current design

We already have the current website, that you can access but we think it can improve from current version.
Veltorquin is a cryptocurrency hedge fund that allow you to participate in the hedge fund with cryptocurrency such as eth.
At current phase, we are doing an ICO, then we want to make sure that the website it looks professional, beautiful and trustable enough for investors after looking at our website.
Target Market(s)
Investors
Industry/Entity Type
Investment
Coding
Coded - Design and coding required
Number of Pages Required
1 page
Look and feel

```html
<!DOCTYPE html>
<html lang="en">
<head>
<meta charset="utf-8">
<title>Veltorquin – Digital Asset Management</title>
<link rel="stylesheet" href="https://fonts.googleapis.com/css2?family=Open+Sans:wght@400;600;700;800&display=swap">
<style>
:root{
  --brand-blue:#0f4f9c;
  --ink:#222;
  --muted:#666;
  --line:#dcdcdc;
  --hero-dark:#2a1608;
  --hero-mid:#6b3d16;
  --gold:#c89a3e;
  --band-dark:#3a200d;
  --band-mid:#6a3e1c;
  --pie-blue:#3a8db3;
  --pie-blue-side:#266a8a;
  --pie-navy:#2e5fa8;
  --pie-red:#b03a3e;
  --pie-green:#8aae3e;
  --pie-green-side:#5f7a28;
  --pie-purple:#5e3f8a;
  --pie-purple-side:#432b66;
}
*{box-sizing:border-box;margin:0;padding:0}
html,body{width:1200px;height:3279px;overflow:hidden;background:#fff}
body{font-family:"Open Sans",Arial,sans-serif;color:var(--ink);position:relative}
section,header,footer{position:absolute;left:0;width:1200px}

/* hero */
.hero{top:0;height:582px;background:radial-gradient(ellipse 420px 380px at 900px 240px,#d9a650 0%,#9a6424 45%,transparent 75%),linear-gradient(180deg,var(--hero-dark),var(--hero-mid) 60%,#3b200c)}
.brand{position:absolute;left:98px;top:50px;display:flex;align-items:center;gap:12px;color:#fff;font-weight:700;font-size:24px}
.brand-dot{width:34px;height:34px;border-radius:50%;background:#fff}
.nav{position:absolute;top:68px;right:100px;display:flex;align-items:center;gap:38px}
.nav a{color:#fff;text-decoration:none;font-size:12px;font-weight:600;letter-spacing:.3px}
.nav .login{border:2px solid #fff;padding:10px 18px;margin-left:-6px}
.hero-title{position:absolute;top:214px;width:100%;text-align:center;color:#fff;font-weight:800;font-size:90px;letter-spacing:2px;line-height:1}
.hero-sub{position:absolute;top:334px;width:100%;text-align:center;color:#fff;font-weight:700;font-size:40px}
.dots{position:absolute;top:527px;left:562px;display:flex;gap:6px}
.dots span{width:11px;height:11px;border-radius:50%;border:2px solid #fff}
.dots span.on{background:#fff}

/* about */
.about{top:582px;height:474px}
.section-title{font-weight:600;font-size:33px;text-transform:uppercase;color:var(--ink)}
.about .section-title{position:absolute;left:98px;top:74px}
.about-text{position:absolute;left:98px;top:136px;width:540px;font-size:12.5px;line-height:30px;color:var(--muted)}
.btn-blue{position:absolute;background:var(--brand-blue);color:#fff;font-size:12px;font-weight:600;text-transform:uppercase;display:flex;align-items:center;justify-content:center}
.about .btn-blue{left:98px;top:351px;width:122px;height:38px}
.about-art{position:absolute;left:667px;top:108px;width:393px;height:228px;border-radius:110px;background:radial-gradient(circle at 50% 45%,#e0ad5c,#a46a28 60%,#fff 100%)}

/* team */
.team{top:1056px;height:566px;background:linear-gradient(135deg,#f6f6f6,#ececec 50%,#f7f7f7)}
.team .section-title{position:absolute;top:77px;width:100%;text-align:center}
.member{position:absolute;top:173px;width:300px;text-align:center}
.member .photo{width:192px;height:192px;border-radius:50%;margin:0 auto;border:5px solid #fff;box-shadow:0 0 0 1px #ccc;background:radial-gradient(circle at 50% 40%,#c9c1b4,#8a8478)}
.member h3{margin-top:27px;font-size:16px;font-weight:600;text-transform:uppercase}
.member p{margin-top:6px;font-size:15px;color:var(--brand-blue)}
.socials{margin-top:10px;display:flex;justify-content:center;gap:5px}
.socials span{width:26px;height:26px;border-radius:50%;background:var(--brand-blue)}

/* process */
.process{top:1622px;height:669px}
.process .section-title{position:absolute;top:84px;width:100%;text-align:center}
.process h4{position:absolute;top:138px;width:100%;text-align:center;font-weight:600;font-size:27px;color:var(--brand-blue)}
.process-text{position:absolute;top:185px;left:220px;width:760px;text-align:center;font-size:12.5px;line-height:30px;color:var(--muted)}
.pie{position:absolute;left:225px;top:310px}
.legend{position:absolute;left:715px;top:374px;list-style:none}
.legend li{display:flex;align-items:center;gap:10px;font-size:12.5px;height:28px}
.legend i{width:14px;height:14px;display:block}

/* cta band */
.cta{top:2291px;height:385px;background:linear-gradient(90deg,var(--band-dark),var(--band-mid) 45%,#4a2a12)}
.cta-art{position:absolute;left:70px;top:0;width:290px;height:385px;background:radial-gradient(ellipse 140px 190px at 145px 200px,#b7b2aa,#6a4a2c 70%,transparent 100%)}
.cta h2{position:absolute;left:393px;top:72px;color:#fff;font-size:38px;font-weight:700}
.cta p{position:absolute;left:393px;top:136px;width:680px;color:#fff;font-size:27px;line-height:44px}
.cta .btn-outline{position:absolute;left:393px;top:251px;width:143px;height:42px;border:2px solid #fff;color:#fff;font-size:13px;font-weight:600;display:flex;align-items:center;justify-content:center}

/* contact */
.contact{top:2676px;height:520px}
.contact .section-title{position:absolute;left:98px;top:73px;font-size:24px}
.field{position:absolute;border:1px solid var(--line);font-size:12px;color:#777;padding:0 15px;display:flex;align-items:center}
.contact .btn-blue{left:98px;top:384px;width:518px;height:46px;letter-spacing:3px;font-weight:700}
.info{position:absolute;left:686px;display:flex;align-items:flex-start;gap:20px;font-size:12px;line-height:21px;color:var(--muted);width:420px}
.info .ico{flex:none;width:52px;height:52px;border-radius:50%;border:1px solid var(--line);display:flex;align-items:center;justify-content:center}
.info-social{position:absolute;left:686px;top:3084px;display:flex;gap:8px}
.info-social span{width:40px;height:40px;border-radius:50%;border:2px solid var(--brand-blue)}
.info-social span:last-child{border-color:#c0392b}

/* footer */
.footer{top:3190px;height:89px}
.footer .rule{margin:0 98px;border-top:1px solid var(--line)}
.footer p{margin-top:35px;text-align:center;font-size:12px;color:var(--muted)}
</style>
</head>
<body>

<header class="hero" role="img" aria-label="Photograph of gold cryptocurrency coins on a dark warm background">
  <div class="brand"><span class="brand-dot"></span>Veltorquin</div>
  <nav class="nav">
    <a href="#">HOME</a><a href="#">ABOUT US</a><a href="#">PROCESS</a><a href="#">TEAM</a><a href="#">CONTACT US</a>
    <a href="#" class="login">&#128274; LOG IN</a>
  </nav>
  <h1 class="hero-title">VELTORQUIN</h1>
  <p class="hero-sub">DIGITAL ASSET MANAGEMENT</p>
  <div class="dots"><span class="on"></span><span></span><span></span><span></span><span></span></div>
</header>

<section class="about">
  <h2 class="section-title">About Veltorquin</h2>
  <p class="about-text">Veltorquin process and manages on hedge fund strategy models which invests in a diversified portfolio of blockchain tokens. Blockchain tokens are emerging which add a monetary incentive layer to p2p protocols and facilitate equity crowdfunding that anyone in the world can participate in. This means open source software developers can monetize their networks at the protocol level and users of the network are the equity owners of the network. For this conditions, returns will go to holders of the tokens.</p>
  <div class="btn-blue">Read More</div>
  <div class="about-art" role="img" aria-label="Pile of gold cryptocurrency coins"></div>
</section>

<section class="team">
  <h2 class="section-title">Meet Executive Team</h2>
  <div class="member" style="left:117px">
    <div class="photo" role="img" aria-label="Portrait photo of the director"></div>
    <h3>Krit Wongsathorn</h3><p>Director</p>
    <div class="socials"><span></span><span></span><span></span><span></span></div>
  </div>
  <div class="member" style="left:429px">
    <div class="photo" role="img" aria-label="Portrait photo of the technical advisor"></div>
    <h3>Natthapon Saelim</h3><p>Technical advisor</p>
    <div class="socials"><span></span><span></span><span></span><span></span></div>
  </div>
  <div class="member" style="left:768px">
    <div class="photo" role="img" aria-label="Portrait photo of the marketing consultant"></div>
    <h3>Chaiwat Boonmeerat</h3><p>Marketing Consultant</p>
    <div class="socials"><span></span><span></span><span></span><span></span></div>
  </div>
</section>

<section class="process">
  <h2 class="section-title">Process</h2>
  <h4>Hedge Fund Model</h4>
  <p class="process-text">Veltorquin run on closed-end fund (CEF) model which offers its shares to investors and utilize the fund to speculate and invest in the innovative blockchain tokens. Veltorquin will charge an upfront annual operation fee 4% of the money raised during the ICO. After that, the fund will charge a quarterly performance of 50% on the net profit made.</p>

  <svg class="pie" width="470" height="300" viewBox="0 0 470 300" font-family="Open Sans, Arial, sans-serif" font-weight="700" fill="#fff">
    <path d="M450 130 A220 120 0 0 1 340 233.9 L340 283.9 A220 120 0 0 0 450 180 Z" fill="var(--pie-green-side)"/>
    <path d="M340 233.9 A220 120 0 0 1 120 233.9 L120 283.9 A220 120 0 0 0 340 283.9 Z" fill="var(--pie-purple-side)"/>
    <path d="M120 233.9 A220 120 0 0 1 10 130 L10 180 A220 120 0 0 0 120 283.9 Z" fill="var(--pie-blue-side)"/>
    <path d="M230 130 L120 233.9 A220 120 0 0 1 230 10 Z" fill="var(--pie-blue)"/>
    <path d="M230 130 L230 10 A220 120 0 0 1 385.6 45.1 Z" fill="var(--pie-navy)"/>
    <path d="M230 130 L385.6 45.1 A220 120 0 0 1 449.2 119.5 Z" fill="var(--pie-red)"/>
    <path d="M230 130 L449.2 119.5 A220 120 0 0 1 340 233.9 Z" fill="var(--pie-green)"/>
    <path d="M230 130 L340 233.9 A220 120 0 0 1 120 233.9 Z" fill="var(--pie-purple)"/>
    <text x="70" y="112" font-size="40">50 %</text>
    <text x="258" y="50" font-size="20">0 – 5 %</text>
    <text x="345" y="95" font-size="20">5 – 10%</text>
    <text x="352" y="168" font-size="28">&gt; 15%</text>
    <text x="185" y="208" font-size="22">10-15 %</text>
  </svg>

  <ul class="legend">
    <li style="color:var(--pie-blue)"><i style="background:var(--pie-blue)"></i>50 % of net profit is distributed to investors</li>
    <li style="color:var(--pie-navy)"><i style="background:var(--pie-navy)"></i>0 – 5 % net profit &gt; 0% performance fee</li>
    <li style="color:var(--pie-red)"><i style="background:var(--pie-red)"></i>5 – 10% net profit &gt; 5% performance fee</li>
    <li style="color:var(--pie-purple)"><i style="background:var(--pie-purple)"></i>10-15 % net profit &gt; 13% performance fee</li>
    <li style="color:var(--pie-green)"><i style="background:var(--pie-green)"></i>&gt; 15% net profit &gt; 15% performance fee</li>
  </ul>
</section>

<section class="cta">
  <div class="cta-art" role="img" aria-label="Stack of silver cryptocurrency coins"></div>
  <h2>VELTORQUIN IS A CRYPTOCURRENCY</h2>
  <p>Hedge fund that allow you to participate in the hedge fund with cryptocurrency such as eth.</p>
  <div class="btn-outline">CLICK HERE</div>
</section>

<section class="contact">
  <h2 class="section-title">Contact Form</h2>
  <div class="field" style="left:98px;top:144px;width:256px;height:48px">First Name</div>
  <div class="field" style="left:360px;top:144px;width:256px;height:48px">Last Name</div>
  <div class="field" style="left:98px;top:196px;width:256px;height:48px">Email *</div>
  <div class="field" style="left:360px;top:196px;width:256px;height:48px">Phone *</div>
  <div class="field" style="left:98px;top:251px;width:518px;height:127px;align-items:flex-start;padding-top:14px">Message</div>
  <div class="btn-blue">Send Message</div>
</section>

<div class="info" style="top:2822px">
  <span class="ico"><svg width="18" height="22" viewBox="0 0 18 22"><path d="M9 1a7 7 0 0 0-7 7c0 5 7 13 7 13s7-8 7-13a7 7 0 0 0-7-7z" fill="var(--brand-blue)"/><circle cx="9" cy="8" r="2.6" fill="#fff"/></svg></span>
  <span>Suite 12-04, 9/F., North Tower, Meridian Trade Plaza, 48 Lantern Road, Kowloon Bay, Hong Kong.</span>
</div>
<div class="info" style="top:2912px">
  <span class="ico"><svg width="20" height="20" viewBox="0 0 20 20"><path d="M4 1l4 4-2 3c1 3 3 5 6 6l3-2 4 4-3 3C9 19 1 11 1 4z" fill="var(--brand-blue)"/></svg></span>
  <span>CALL US NOW !<br>(555) - 210 - 4836</span>
</div>
<div class="info" style="top:2986px">
  <span class="ico"><svg width="20" height="16" viewBox="0 0 20 16"><rect x="1" y="1" width="18" height="14" rx="2" fill="var(--brand-blue)"/><path d="M2 3l8 6 8-6" stroke="#fff" stroke-width="1.6" fill="none"/></svg></span>
  <span>MAIL US :<br>hello@veltorquin.io</span>
</div>
<div class="info-social"><span></span><span></span><span></span><span></span></div>

<footer class="footer">
  <div class="rule"></div>
  <p>© copyright 2017 Veltorquin . All rights reserved</p>
</footer>

</body>
</html>
```